Nutrition Infographic for weight loss- key points and nutrition habits for after weight loss surgery

I need someone to put together some infographics based on some nutrition information I have put together. We are a company who do weight loss surgery for patients and I am trying to put together some resources for patients so they can look after their nutrition for the long term.

I have some info and ideas on how we can execute this on paper but I need some a creative genius with top notch design skills to help me put it together.

I am basically after two infographics- One with the nutrition information I have outlined and One with the pyramid I have illustrated. Please let me know if you need clarification on the layout. Also happy to take on board any ideas you might have too!

If more time is needed with adjustments/refinements I understand and am happy to work with you to get to a final product we are happy with.

Target Market(s)

weight loss clients- ages ranging mostly from 20-45 male and female.

Industry/Entity Type

Health Care

Colors

Designer to choose colors to be used in the design.

Requirements
Must have
• Simple, clean concepts and images are needed.
• Easy to understand layout to enhance uptake of understanding the information

```html
<!DOCTYPE html>
<html lang="en">
<head>
<meta charset="utf-8">
<title>Good Nutrition Habits for Life</title>
<link rel="stylesheet" href="https://fonts.googleapis.com/css2?family=Amaranth:wght@700&family=Oswald:wght@400&family=Roboto:wght@500&display=swap">
<style>
  :root {
    --orange: #f7941d;
    --mint: #aeeadb;
    --teal: #5fd3bf;
    --white: #ffffff;
    --ribbon: #f4f4f2;
    --plate: #59c6ea;
    --plate-rim: #e9f7f4;
  }
  * { margin: 0; padding: 0; box-sizing: border-box; }
  html, body { width: 1200px; height: 1154px; overflow: hidden; }
  body { background: var(--orange); font-family: "Roboto", Arial, sans-serif; }
  .infographic {
    position: relative; width: 1200px; height: 1154px;
    border: 15px solid var(--orange); border-bottom: 0;
    background: var(--mint); overflow: hidden;
  }
  .title-ribbon { position: absolute; left: 76px; top: 36px; width: 1016px; height: 75px; }
  .title {
    position: absolute; left: 76px; top: 36px; width: 1016px; height: 75px;
    display: flex; align-items: center; justify-content: center;
    font-family: "Amaranth", "Trebuchet MS", sans-serif; font-weight: 700;
    font-size: 60px; color: var(--orange); letter-spacing: 0.5px;
  }
  .panel { position: absolute; background: var(--teal); border-radius: 4px 22px 22px 4px; color: var(--white); }
  .intro { left: 31px; top: 163px; width: 1123px; height: 253px; padding: 22px 12px 0 12px; }
  .intro p, .everyday p { font-size: 20.5px; line-height: 26.5px; }
  .intro .narrow { width: 900px; }
  .everyday { left: 31px; top: 453px; width: 1123px; height: 92px; padding: 14px 12px 0 12px; }
  .group-label {
    position: absolute; left: 0; width: 232px; text-align: center;
    font-family: "Oswald", "Arial Narrow", sans-serif; font-size: 33px; line-height: 46px;
    transform: scaleX(0.85);
  }
  .proteins { left: 31px; top: 582px; width: 1115px; height: 153px; }
  .dairy { left: 31px; top: 773px; width: 737px; height: 161px; }
  .produce { left: 31px; top: 976px; width: 949px; height: 163px; }
  .item { position: absolute; text-align: center; }
  .item .art { display: block; margin: 0 auto; }
  .item span { display: block; font-size: 21px; line-height: 24px; margin-top: 4px; }
</style>
</head>
<body>
<main class="infographic">
  <svg class="title-ribbon" viewBox="0 0 1016 75" aria-hidden="true">
    <polygon points="0,0 1016,0 990,37 1016,75 0,75 26,37" fill="var(--ribbon)"/>
  </svg>
  <h1 class="title">Good Nutrition Habits for Life</h1>

  <section class="panel intro">
    <p>Healthy Eating has become very confusing these days with everyone claiming to be an expert in nutrition. You have taken steps to lose weight and look after your health so we can take this opportunity to create some good nutrition habits for now and for the long term.</p>
    <p>You will learn about food again and the healthy balance we can achieve to eat in a way which is going to be sustainable in the long term- There is no sense in depriving your body or over-restricting yourself- on the contrary it will be about nourishing your body with the right types of food to keep you satisfied and to fuel your body for journey ahead.</p>
    <p class="narrow">To make things easier we are going to breakdown different food groups and prioritise them based on how much your body needs them.</p>
  </section>

  <section class="panel everyday">
    <p>EVERYDAY FOODS- Include these on a regular basis as they are generally whole foods, less processed and high in nutrient quality. There is no substitute for the naturally occurring vitamins, minerals and anti-oxidants which we find in food.</p>
  </section>

  <section class="panel proteins">
    <h2 class="group-label" style="top:28px">HIGH QUALITY<br>PROTEINS</h2>
    <div class="item" style="left:276px;top:12px;width:110px">
      <svg class="art" width="108" height="108" role="img" aria-label="Roast chicken illustration"><circle cx="54" cy="54" r="52" fill="var(--plate-rim)"/><circle cx="54" cy="58" r="36" fill="#c8772b"/></svg><span>Chicken</span></div>
    <div class="item" style="left:426px;top:12px;width:110px">
      <svg class="art" width="108" height="108" role="img" aria-label="Raw meat steak illustration"><circle cx="54" cy="54" r="52" fill="var(--plate-rim)"/><rect x="6" y="32" width="96" height="46" rx="6" fill="#b85a5a"/></svg><span>Meat</span></div>
    <div class="item" style="left:566px;top:12px;width:110px">
      <svg class="art" width="118" height="108" role="img" aria-label="Minced meat on a plate illustration"><ellipse cx="59" cy="58" rx="58" ry="40" fill="var(--plate)"/><ellipse cx="59" cy="52" rx="44" ry="26" fill="#e8a99a"/></svg><span>Mince</span></div>
    <div class="item" style="left:707px;top:12px;width:110px">
      <svg class="art" width="108" height="108" role="img" aria-label="Salmon fillet illustration"><circle cx="54" cy="54" r="52" fill="var(--plate-rim)"/><circle cx="54" cy="54" r="40" fill="#f07a50"/></svg><span>Fish</span></div>
    <div class="item" style="left:847px;top:12px;width:110px">
      <svg class="art" width="118" height="108" role="img" aria-label="Shrimp, mussels and squid on a plate illustration"><ellipse cx="59" cy="58" rx="58" ry="40" fill="var(--plate)"/><ellipse cx="59" cy="50" rx="38" ry="28" fill="#f0a45c"/></svg><span>Seafood</span></div>
    <div class="item" style="left:987px;top:12px;width:110px">
      <svg class="art" width="118" height="108" role="img" aria-label="Fried egg and sausages on a plate illustration"><ellipse cx="59" cy="58" rx="58" ry="40" fill="var(--plate)"/><ellipse cx="59" cy="50" rx="38" ry="26" fill="#f7e3c0"/></svg><span>Eggs</span></div>
  </section>

  <section class="panel dairy">
    <h2 class="group-label" style="top:55px">DAIRY</h2>
    <div class="item" style="left:276px;top:6px;width:120px">
      <svg class="art" width="118" height="120" role="img" aria-label="Milk bottle and glass illustration"><ellipse cx="59" cy="82" rx="58" ry="36" fill="var(--plate)"/><rect x="34" y="8" width="44" height="86" rx="8" fill="#eef3f7"/></svg><span>Milk</span></div>
    <div class="item" style="left:416px;top:6px;width:120px">
      <svg class="art" width="118" height="120" role="img" aria-label="Wedge of cheese illustration"><ellipse cx="59" cy="82" rx="58" ry="36" fill="var(--plate)"/><rect x="12" y="34" width="94" height="50" rx="4" fill="#fbd04a"/></svg><span>Chesse</span></div>
    <div class="item" style="left:556px;top:6px;width:120px">
      <svg class="art" width="118" height="120" role="img" aria-label="Yoghurt cups illustration"><ellipse cx="59" cy="82" rx="58" ry="36" fill="var(--plate)"/><rect x="20" y="10" width="78" height="86" rx="10" fill="#f3f3f3"/></svg><span>Yoghurt</span></div>
  </section>

  <section class="panel produce">
    <h2 class="group-label" style="top:28px">FRUIT<br>VEGETABLES</h2>
    <div class="item" style="left:283px;top:8px;width:194px">
      <svg class="art" width="194" height="106" role="img" aria-label="Watermelon, strawberries and kiwi illustration"><rect x="0" y="4" width="194" height="98" rx="49" fill="#6fb840"/></svg><span>Fruits</span></div>
    <div class="item" style="left:513px;top:8px;width:110px">
      <svg class="art" width="100" height="106" role="img" aria-label="Glass of orange juice with oranges illustration"><rect x="10" y="0" width="80" height="102" rx="12" fill="#f7a21d"/></svg><span>Fruit Juice</span></div>
    <div class="item" style="left:680px;top:8px;width:234px">
      <svg class="art" width="232" height="106" role="img" aria-label="Assorted fresh vegetables illustration"><rect x="0" y="4" width="232" height="98" rx="49" fill="#5aa63a"/></svg><span>Vegetables</span></div>
  </section>
</main>
</body>
</html>
```